Business card

I need a business card design for my consulting company in animal welfare for livestock. I like clean, crisp, simple.

One I imagined was double-sided:
side1: just my name and contact information
side2: silhouette of farm animals. Could be 3 (pig, cow, chicken) or all the species (pig, cow, chicken, duck, sheep, rabbit, etc) that continue the length of the card. I have attached an image of a silhouette style.

But, I am open to any concept.

Industry/Entity Type

Business

```html
<!DOCTYPE html>
<html lang="en">
<head>
<meta charset="utf-8">
<title>Clara Whitfield — Business Card</title>
<link rel="stylesheet" href="https://fonts.googleapis.com/css2?family=PT+Sans&family=Arimo:wght@700&family=Tinos&display=swap">
<style>
  :root {
    --stage: #ecebe7;
    --brand-blue: #0565ad;
    --brand-green: #037c3a;
    --band-green: #0a9a3f;
    --stripe-green: #079040;
    --stripe-white: #ffffff;
    --accent-yellow: #f5ef13;
    --text-white: #ffffff;
    --back-green: #009640;
    --silhouette: #0c0c0e;
  }
  * { box-sizing: border-box; margin: 0; padding: 0; }
  html, body { width: 1200px; height: 888px; overflow: hidden; }
  body { background: var(--stage); position: relative; }

  .card {
    position: absolute;
    width: 640px;
    height: 384px;
    overflow: hidden;
    box-shadow: 0 6px 18px rgba(0, 0, 0, 0.25);
  }
  .card-front { left: 60px; top: 40px; }
  .card-back { left: 500px; top: 464px; background: var(--back-green); }

  .front-pattern { position: absolute; inset: 0; width: 100%; height: 100%; }

  .front-text { position: absolute; inset: 0; color: var(--text-white); }
  .holder-name {
    position: absolute; left: 0; right: 0; top: 124px;
    text-align: center;
    font-family: "PT Sans", sans-serif;
    font-size: 46px; font-weight: 400; line-height: 1;
  }
  .tagline {
    position: absolute; left: 0; right: 0; top: 186px;
    text-align: center;
    font-family: "Arimo", sans-serif;
    font-weight: 700; font-size: 21px;
    color: var(--accent-yellow);
  }
  .contact {
    position: absolute; left: 147px; top: 224px;
    font-family: "Tinos", serif;
    font-size: 22px; line-height: 29px;
  }
  .contact-row { display: flex; }
  .contact-label { width: 66px; }

  .livestock-silhouette {
    position: absolute;
    left: 150px; top: 24px;
    width: 350px; height: 272px;
    background: var(--silhouette);
    border-radius: 60px 40px 10px 10px;
  }
</style>
</head>
<body>
  <section class="card card-front">
    <svg class="front-pattern" viewBox="0 0 706 424" preserveAspectRatio="none" aria-hidden="true">
      <!-- top section -->
      <rect x="0" y="0" width="706" height="95" fill="var(--brand-green)"/>
      <polygon points="0,0 262,0 284,95 0,95" fill="var(--brand-blue)"/>
      <polygon points="262,0 345,0 367,95 284,95" fill="var(--stripe-white)"/>
      <!-- middle section -->
      <rect x="0" y="95" width="706" height="233" fill="var(--brand-blue)"/>
      <polygon points="0,95 284,95 337,328 0,328" fill="var(--brand-green)"/>
      <polygon points="284,95 367,95 421,328 337,328" fill="var(--stripe-green)"/>
      <!-- bottom section -->
      <rect x="0" y="328" width="706" height="96" fill="var(--brand-green)"/>
      <polygon points="0,328 337,328 360,424 0,424" fill="var(--brand-blue)"/>
      <polygon points="337,328 421,328 445,424 360,424" fill="var(--stripe-white)"/>
      <!-- dividing bands -->
      <rect x="0" y="95" width="706" height="13" fill="var(--band-green)"/>
      <rect x="0" y="315" width="706" height="13" fill="var(--band-green)"/>
    </svg>
    <div class="front-text">
      <h1 class="holder-name">Clara Whitfield</h1>
      <p class="tagline">Welfare Services for Livestock Stakeholders</p>
      <div class="contact">
        <div class="contact-row"><span class="contact-label">Email</span><span>: clara.whitfield@mailbox.com</span></div>
        <div class="contact-row"><span class="contact-label">Tel</span><span>: +1.604.555.0172</span></div>
      </div>
    </div>
  </section>

  <section class="card card-back">
    <div class="livestock-silhouette" role="img" aria-label="Black silhouette of a dairy cow standing in profile"></div>
  </section>
</body>
</html>
```